Single-sided business card for restaurant bellamonte with new logo made on this site

Business card options with new logo including restaurant name, address, phone number and website. This business card is single-sided only and will be presented at the hostess desk for clients to take. I would like to see options based on a cream card background, a white card background, a yellow card background and a burgundy colored background. It needs to be elegant and traditional.

Target Market(s)

local and international crowd

Industry/Entity Type

restaurant

Contact Information for Business Card

address, website and phone number

Font styles to use
Serif

Colors
EE7325
F08F49
F5BC92
FAE3D3
FDF4ED

Requirements
Must have
• new logo, address, phone number, website
Should not have
• more than three colors

```html
<!DOCTYPE html>
<html lang="es">
<head>
<meta charset="utf-8">
<title>Bellamonte — Tarjeta de presentación</title>
<link href="https://fonts.googleapis.com/css2?family=Montserrat:wght@400&display=swap" rel="stylesheet">
<style>
  :root {
    --backdrop: #262626;
    --cream: #fdebcc;
    --burgundy: #331317;
    --gold: #f0b42a;
    --card-text: #ffffff;
    --brand-brown: #3a1a17;
  }
  html, body {
    margin: 0;
    padding: 0;
    width: 1200px;
    height: 800px;
    overflow: hidden;
    background: var(--backdrop);
  }
  .canvas {
    position: relative;
    width: 1200px;
    height: 800px;
  }
  .business-card {
    position: absolute;
    left: 75px;
    top: 102px;
    width: 952px;
    height: 540px;
    transform: scale(1.103);
    transform-origin: top left;
    background: var(--cream);
    overflow: hidden;
  }
  .card-swoosh {
    position: absolute;
    inset: 0;
    width: 952px;
    height: 540px;
  }
  .swoosh-gold { fill: var(--gold); }
  .swoosh-edge { fill: none; stroke: #ffffff; stroke-width: 2; }
  .swoosh-panel { fill: var(--burgundy); }

  .brand {
    position: absolute;
    left: 60px;
    top: 245px;
    width: 360px;
    display: flex;
    align-items: center;
    justify-content: center;
    gap: 14px;
  }
  .brand-dot {
    width: 30px;
    height: 30px;
    border-radius: 50%;
    background: var(--gold);
    flex: none;
  }
  .brand-name {
    margin: 0;
    font-family: 'Montserrat', sans-serif;
    font-weight: 400;
    font-size: 40px;
    line-height: 1;
    color: var(--brand-brown);
  }

  .contact {
    position: absolute;
    right: 70px;
    top: 276px;
    text-align: right;
    font-family: 'Montserrat', sans-serif;
    font-weight: 400;
    font-size: 21px;
    line-height: 26.5px;
    color: var(--card-text);
  }
  .contact p { margin: 0; }
  .contact .address { margin-bottom: 10px; }
  .contact .reservations { margin-bottom: 12px; }
</style>
</head>
<body>
<div class="canvas">
  <div class="business-card">
    <svg class="card-swoosh" viewBox="0 0 952 540" aria-hidden="true">
      <path class="swoosh-gold" d="M714,0 L740,0 C690,50 650,140 600,240 C520,400 420,500 275,540 L250,540 C395,500 488,400 572,240 C628,130 668,40 714,0 Z"/>
      <path class="swoosh-edge" d="M714,0 C668,40 628,130 572,240 C488,400 395,500 250,540"/>
      <path class="swoosh-panel" d="M740,0 L952,0 L952,540 L275,540 C420,500 520,400 600,240 C650,140 690,50 740,0 Z"/>
    </svg>

    <div class="brand">
      <span class="brand-dot"></span>
      <p class="brand-name">Bellamonte</p>
    </div>

    <div class="contact">
      <div class="address">
        <p>Restaurant Bella-Monte</p>
        <p>Jacaranda 415</p>
        <p>Puerto Escondido</p>
        <p>Oaxaca CP 71980</p>
      </div>
      <div class="reservations">
        <p>Reservaciones</p>
        <p>954-312-7740</p>
      </div>
      <p class="website">www.bellamonte.com.mx</p>
    </div>
  </div>
</div>
</body>
</html>
```